Clinician Harbor Collective

I am a financial planner whose client's are physicians and dentists. As physicians, there is very little time for them to do research on numerous aspects of their business and personal lives. I am looking to build a website that is a 1 stop shop for many of the services/resources they may need. It will be my job to screen the resources/advertisers and place competent people/business's that I know and have a track record on. there will ultimately be 10 or 12 ish areas that I would like to provide resources in:
disability insurance
life insurance
retirement planning
student loan advisors
employment contract and business formation attorneys
accountants
real estate agents
physician mortgages
personal loans
malpractice insurance
physician recruiters
maybe 2 other areas which I have yet to figure out.....
I would like each of these options to be able to be clicked on and a page will open up with the 1 or 2 or 3 or 4 people/business's that I have picked to represent these areas. I would like each specific person/business to have a click here to contact me link in which an email goes to the person and I am copied on the initial correspondence between the physician and the mortgage broker.... just so I can see some of the correspondence they will be receiving.
nowhere on the site do I want it to say my name. there will be certain disclosures that are needed and other wording but I think this is a good starting point.
here are links to two websites with the same general concept. please keep in mind that I want my website to be more on the simple side.
http://www.vantorelmedlink.example/index.html
http://bluestethwealth.example/
Industry/Entity Type
Financial

```html
<!DOCTYPE html>
<html lang="en">
<head>
<meta charset="utf-8">
<title>Clinician Harbor Collective</title>
<link href="https://fonts.googleapis.com/css2?family=Roboto+Condensed:wght@300;400;700&family=Arimo:wght@400&display=swap" rel="stylesheet">
<style>
:root{
  --blue:#2c5d95;
  --green:#5b9a57;
  --red:#a3172d;
  --ink:#333;
  --panel:#f1f1f1;
  --line:#dcdcdc;
  --foot-top:#2b2b2b;
  --foot:#1f1f1f;
  --foot-text:#8a8a8a;
}
*{margin:0;padding:0;box-sizing:border-box}
html,body{width:756px;height:1200px;overflow:hidden;background:#fff}
body{font-family:"Roboto Condensed","Arial Narrow",sans-serif;color:var(--ink)}
.page{position:relative;width:756px;height:1200px;overflow:hidden}
.abs{position:absolute}
.ph{position:absolute}
.nw{white-space:nowrap}
/* header */
.topline{left:0;top:0;width:756px;height:3px;background:#222}
.header{left:0;top:3px;width:756px;height:46px;background:linear-gradient(#fff,#f4f4f4);border-bottom:1px solid #e2e2e2}
.brand{left:29px;top:12px;font-size:20px;font-weight:400;color:var(--blue);letter-spacing:-.3px;white-space:nowrap}
.nav{right:30px;top:3px;display:flex;height:45px}
.nav a{display:block;padding:0 11px;line-height:45px;font-family:Arimo,sans-serif;font-size:10.5px;color:#444;text-decoration:none;white-space:nowrap}
.nav a.current{color:var(--blue);border:1px solid #dcdcdc;border-bottom:2px solid var(--blue);background:#fff;line-height:42px}
/* hero */
.hero{left:29px;top:61px;width:519px;height:266px;background:linear-gradient(100deg,#c9d6df 0%,#e6ecef 45%,#f3f1ee 70%,#dfe4e8 100%)}
.hero-cap{left:29px;top:245px;width:303px;height:64px;background:rgba(40,40,40,.78);padding:9px 16px;overflow:hidden;white-space:nowrap}
.hero-cap h1{font-weight:400;font-size:26px;color:#fff;line-height:30px;letter-spacing:-.5px}
.hero-cap p{font-size:11.5px;line-height:15px;color:#ddd;font-weight:300}
.side{left:557px;width:169px;height:82px;border:1px solid #e2e2e2;background:#fafafa}
.side .img{position:absolute;top:4px;height:74px}
.side .t{position:absolute;text-align:center;line-height:17px;white-space:nowrap}
/* thumbs */
.thumb{top:346px;width:160px;height:101px}
.thumb .img{position:absolute;inset:0}
.thumb span{position:absolute;left:0;right:0;bottom:0;height:24px;background:rgba(45,45,45,.8);color:#fff;text-align:center;font-size:12.5px;line-height:24px;white-space:nowrap}
/* service tiles */
.tile{left:29px;width:220px;height:96px;overflow:hidden}
.tile svg{position:absolute;inset:0}
.tile .label{position:absolute;color:#fff;font-size:16px;line-height:19px;white-space:nowrap}
.tile .label b{font-weight:400;display:block}
.tile .label i{font-style:normal;font-weight:300;font-size:14px}
.attys{text-align:center;color:var(--green);font-size:14.5px;line-height:21px;padding-top:17px;font-weight:300;letter-spacing:-.3px;white-space:nowrap}
/* content */
.h2{font-size:20px;font-weight:400;color:#222;letter-spacing:-.3px;white-space:nowrap}
.h2 em{font-style:normal;color:var(--blue)}
.rule{height:1px;background:var(--line)}
.rule::before{content:"";display:block;width:86px;height:2px;background:#c45;margin-top:-1px}
.copy{left:268px;top:507px;width:458px;font-size:9.7px;line-height:13.5px;color:#333}
.copy p{margin-bottom:13px}
.quotes{left:268px;top:797px;width:458px;height:205px;background:var(--panel);border:1px solid #e4e4e4;padding:14px 22px 0 24px}
.q{position:relative;font-size:9.7px;line-height:15.2px;color:#555;padding-left:10px}
.q .o,.q .c{color:var(--blue);font-size:20px;font-weight:700;line-height:0;font-family:Arimo,sans-serif}
.q .o{position:absolute;left:-10px;top:12px}
.q .c{position:relative;top:8px;margin-left:2px}
.who{text-align:right;font-size:10px;color:#222;margin:10px 0 22px}
/* footer */
.ftop{left:0;top:1009px;width:756px;height:29px;background:var(--foot-top)}
.flinks{left:30px;top:1009px;line-height:29px;font-family:Arimo,sans-serif;font-size:8px;color:#bbb;white-space:nowrap}
.social{top:1015px;width:16px;height:16px;border-radius:2px}
.fmain{left:0;top:1038px;width:756px;height:162px;background:var(--foot)}
.fcol{top:1051px;width:113px}
.fcol h4{font-weight:400;font-size:9.5px;color:#aaa;margin-bottom:6px}
.fcol li{list-style:none;font-family:Arimo,sans-serif;font-size:7px;color:var(--foot-text);height:17px;line-height:16px;border-bottom:1px dashed #3a3a3a;white-space:nowrap;overflow:hidden}
.fcol li::before{content:"› ";color:#aaa}
.field{left:545px;width:179px;background:#151515;border:1px solid #2c2c2c;font-family:Arimo,sans-serif;font-size:7.5px;color:#555;padding:6px 8px}
.btn{left:545px;top:1167px;width:82px;height:19px;background:linear-gradient(#f5f5f5,#cfcfcf);border-radius:2px;text-align:center;font-family:Arimo,sans-serif;font-size:8.5px;line-height:19px;color:#222;white-space:nowrap}
.legal{left:30px;top:1181px;font-family:Arimo,sans-serif;font-size:7px;color:#444;white-space:nowrap}
</style>
</head>
<body>
<div class="page">
  <div class="abs topline"></div>
  <header class="abs header"></header>
  <div class="abs brand">Clinician Harbor Collective</div>
  <nav class="abs nav">
    <a class="current" href="#">Home</a><a href="#">About Us</a><a href="#">Services</a><a href="#">News</a><a href="#">Contact Us</a>
  </nav>

  <div class="ph hero" role="img" aria-label="Smiling young physician in a white coat with a stethoscope, colleagues blurred in a hospital corridor behind"></div>
  <div class="abs hero-cap"><h1>LOREM IPSUM IS SIMPLY</h1><p>It is a long established fact that a reader will be</p></div>

  <div class="abs side" style="top:61px">
    <div class="img" role="img" aria-label="Wheelchair" style="left:4px;width:60px;background:linear-gradient(#e4e4e4,#bdbdbd)"></div>
    <div class="t" style="left:72px;top:22px;width:94px;font-size:14px"><span style="color:var(--blue)">DISABILITY</span><br><span style="color:#222">INSURANCE</span></div>
  </div>
  <div class="abs side" style="top:153px;background:#f2f2f2">
    <div class="t" style="left:3px;top:16px;width:90px;font-size:14px"><span style="color:var(--green)">LIFE</span><br><span style="color:#222">INSURANCE</span></div>
    <div class="img" role="img" aria-label="Cupped hands holding a paper cut-out family" style="left:96px;width:68px;background:linear-gradient(#f0e3d6,#d9b396)"></div>
  </div>
  <div class="abs side" style="top:245px;background:#fff">
    <div class="img" role="img" aria-label="Smiling support agent wearing a headset" style="left:0;top:0;height:80px;width:62px;background:linear-gradient(#c98d5f,#6f3f25)"></div>
    <div class="t" style="left:66px;top:26px;width:102px;line-height:19px"><span style="color:var(--red);font-size:17px">CALL US</span><br><span style="color:#222;font-size:14px">000-0000-0000</span></div>
  </div>

  <div class="abs thumb" style="left:29px"><div class="img" role="img" aria-label="Retired couple in deck chairs on a beach" style="background:linear-gradient(#cfe4ef,#e8e2d3)"></div><span>Retirement Planning</span></div>
  <div class="abs thumb" style="left:208px"><div class="img" role="img" aria-label="Student with glasses in a library" style="background:linear-gradient(90deg,#c9b7a0,#e9e2d8)"></div><span>Student Loan Advisors</span></div>
  <div class="abs thumb" style="left:387px"><div class="img" role="img" aria-label="Accountants reviewing documents together" style="background:linear-gradient(90deg,#d7dde2,#f3f3f3)"></div><span>Accountants</span></div>
  <div class="abs thumb" style="left:566px"><div class="img" role="img" aria-label="Excited woman holding a fan of banknotes" style="background:linear-gradient(90deg,#c99a78,#e9ece6)"></div><span>Personal Loans</span></div>

  <div class="abs tile" style="top:478px">
    <svg width="220" height="96"><rect width="220" height="96" fill="#c8ccc4" role="img" aria-label="Real estate agent with a clipboard beside a for-sale sign"/><polygon points="155,0 220,0 220,96 99,96" fill="var(--green)"/></svg>
    <div class="label" style="right:8px;top:34px;text-align:center"><b>REAL ESTATE</b><i>Agents</i></div>
  </div>
  <div class="abs tile" style="top:585px">
    <svg width="220" height="96"><rect width="220" height="96" fill="#eed9a6" role="img" aria-label="Insurance policy document with glasses and a pen"/><polygon points="0,0 70,0 123,96 0,96" fill="var(--blue)"/></svg>
    <div class="label" style="left:3px;top:36px"><b>MALPRACTICE</b><i style="margin-left:12px">Insurance</i></div>
  </div>
  <div class="abs tile" style="top:691px">
    <svg width="220" height="96"><rect width="220" height="96" fill="#dfe3e7" role="img" aria-label="Group of doctors and nurses in white coats and scrubs"/><polygon points="155,0 220,0 220,96 99,96" fill="var(--green)"/></svg>
    <div class="label" style="right:12px;top:34px;text-align:center"><b>PHYSICIAN</b><i>Recruiters</i></div>
  </div>
  <div class="abs tile" style="top:798px;background:var(--panel);border:1px solid #e2e2e2">
    <div class="label" style="left:17px;top:31px;color:var(--blue)"><b>PHYSICIAN</b><i style="color:#222">Mortgages</i></div>
    <div class="ph" role="img" aria-label="Small red house balanced on a seesaw against a percent sign" style="left:95px;top:18px;width:118px;height:70px;background:linear-gradient(90deg,#f1f1f1,#e0c8a8)"></div>
  </div>
  <div class="abs tile attys" style="top:906px;background:var(--panel);border:1px solid #e2e2e2">EMPLOYMENT CONTRACT<br>AND<br>BUSINESS FORMATION ATTORNEYS</div>

  <div class="abs h2" style="left:268px;top:473px">Welcome to <em>Clinician Harbor Collective</em></div>
  <div class="abs rule" style="left:268px;top:499px;width:458px"></div>
  <div class="abs copy">
    <p>Lorem ipsum dolor sit amet, consectetur adipiscing elit. Donec eu ante sit amet risus convallis scelerisque. Fusce fermentum in mauris eget scelerisque. Nunc in ornare neque. Aliquam at nulla nibh. Aenean consectetur a libero non aliquet. Fusce pulvinar vestibulum quam vitae gravida. Ut vitae quam ac tortor ultrices iaculis quis eget nulla. Quisque non pulvinar dolor, ut pretium massa. Vivamus convallis, tellus at fermentum ultricies, lacus urna accumsan nunc, ac accumsan libero lacus nec urna. Ut vel sapien feugiat, eleifend metus a, tincidunt lorem. Suspendisse sed eget erat eget tortor tincidunt eleifend.</p>
    <p>Aliquam tincidunt sit amet augue sed condimentum. Praesent suscipit porttitor egestas. Praesent hendrerit odio tortor, eu feugiat ipsum tristique quis. Proin risus augue, tincidunt quis scelerisque id, aliquam et velit. Donec rutrum est eget nunc facilisis consectetur. Nunc et ex rutrum, luctus est et, aliquam diam. Sed ac arcu leo. Suspendisse sed elit sodales, interdum leo a, eleifend urna. Nulla hendrerit venenatis interdum.</p>
    <p>In dignissim viverra lacus vitae pellentesque. Aliquam at fringilla leo, vel molestie enim. Nulla rhoncus pellentesque massa quis laoreet. Curabitur nec suscipit lorem, quis pretium orci. Pellentesque fringilla facilisis sapien, ac vulputate eros mattis commodo. Fusce enim massa, tincidunt ut sem vel, tincidunt vehicula massa. Sed vulputate ante ut velit vehicula, eget feugiat felis porta. Donec vel mi tempus, lacinia quam non, dapibus sem. Fusce a ante dignissim velit porttitor malesuada. Aliquam sed dolor diam. Aenean commodo ex ac libero interdum ultrices eget quis sem.</p>
  </div>

  <div class="abs h2" style="left:268px;top:759px">Our <em>Client Say</em></div>
  <div class="abs rule" style="left:268px;top:785px;width:458px"></div>
  <div class="abs quotes">
    <div class="q"><span class="o">“</span>There are many variations of passages of Lorem Ipsum available, but the majority have suffered alteration in some form, by injected humour, or randomised words which don't look even slightly believable. If you are going to use a passage of Lorem Ipsum, you need to be sure there.<span class="c">”</span></div>
    <div class="who">----- &nbsp;Client Name Here</div>
    <div class="q"><span class="o">“</span>There are many variations of passages of Lorem Ipsum available, but the majority have suffered alteration in some form, by injected humour, or randomised words which don't look even slightly believable. If you are going to use a passage of Lorem Ipsum, you need to be sure there.<span class="c">”</span></div>
    <div class="who">----- &nbsp;Client Name Here</div>
  </div>

  <div class="abs ftop"></div>
  <div class="abs flinks">Home &nbsp;| &nbsp;About &nbsp;| &nbsp;Service &nbsp;| &nbsp;News &nbsp;| &nbsp;Contact Us</div>
  <div class="abs social" style="left:647px;background:#3b63a8"></div>
  <div class="abs social" style="left:668px;background:#3f5571"></div>
  <div class="abs social" style="left:690px;background:#f08a16"></div>
  <div class="abs social" style="left:711px;background:#d33a2c"></div>

  <div class="abs fmain"></div>
  <div class="abs fcol" style="left:29px"><h4>Services 1</h4><ul><li>There are many</li><li>Variations of passages Lorem</li><li>Ipsum available</li><li>Majority have suffered Alteration</li><li>in some</li><li>Injected humour</li></ul></div>
  <div class="abs fcol" style="left:209px"><h4>Services 1</h4><ul><li>There are many</li><li>Variations of passages Lorem</li><li>Ipsum available</li><li>Majority have suffered Alteration</li><li>in some</li><li>Injected humour</li></ul></div>
  <div class="abs fcol" style="left:387px"><h4>Services 1</h4><ul><li>There are many</li><li>Variations of passages Lorem</li><li>Ipsum available</li><li>Majority have suffered Alteration</li><li>in some</li><li>Injected humour</li></ul></div>
  <div class="abs fcol" style="left:545px"><h4>Quick contact</h4></div>
  <div class="abs field" style="top:1072px;height:23px">Your Email</div>
  <div class="abs field" style="top:1103px;height:56px">Comments</div>
  <div class="abs btn">Send Feedback</div>
  <div class="abs legal">Company Name © 2014. Privacy Policy</div>
</div>
</body>
</html>
```